Namecard and logo for New startup cloud communication company

We need name card and logo deign for our company

company name Zol Quendaro Pte Ltd
Its a cloud base company offering IP PBX communication solutions
Young start up company base in Singapore with experience in asterisk solutions

We require the design to be unique and updated
to incorporate Zol and Cloud into the design.

Industry/Entity Type

Communication

Contact Information for Business Card

We require the following on name card

Company name
Name
Company address
Mobile Number and main line with ext
email address
website address

Font styles to use
Sans Serif

```html
<!DOCTYPE html>
<html lang="en">
<head>
<meta charset="utf-8">
<title>Zol Quendaro – Name Card</title>
<link href="https://fonts.googleapis.com/css2?family=Questrial&display=swap" rel="stylesheet">
<style>
  :root {
    --brand-blue: #1f86c3;
    --card-blue: #2a8cc4;
    --card-blue-soft: #3596cc;
    --ink-grey: #5d5f66;
    --paper: #ffffff;
    --cloud-grey: #e9ebee;
    --backdrop: #e8e7ed;
  }
  * { margin: 0; padding: 0; box-sizing: border-box; }
  html, body {
    width: 1200px;
    height: 934px;
    overflow: hidden;
  }
  body {
    position: relative;
    background: var(--backdrop);
    font-family: "Questrial", "Century Gothic", sans-serif;
    color: var(--ink-grey);
  }

  /* standalone brand lockup */
  .brand-lockup {
    position: absolute;
    top: 80px;
    right: 96px;
    width: 290px;
    text-align: center;
  }
  .brand-mark {
    display: flex;
    align-items: center;
    justify-content: center;
    gap: 12px;
  }
  .brand-dot {
    width: 22px;
    height: 22px;
    border-radius: 50%;
    background: var(--brand-blue);
    flex: none;
  }
  .brand-name {
    font-size: 34px;
    letter-spacing: 1px;
    color: var(--brand-blue);
    white-space: nowrap;
  }
  .brand-url {
    margin-top: 6px;
    font-size: 17px;
    color: var(--ink-grey);
  }

  /* cards */
  .card {
    position: absolute;
    width: 500px;
    height: 290px;
    overflow: hidden;
    box-shadow: 0 6px 18px rgba(60, 60, 80, 0.12);
  }
  .card-back {
    left: 90px;
    top: 330px;
    background: var(--card-blue);
  }
  .card-front {
    left: 610px;
    top: 330px;
    background: var(--paper);
  }
  .card-decor {
    position: absolute;
    inset: 0;
    width: 100%;
    height: 100%;
  }

  .card-back .card-logo {
    position: absolute;
    left: 70px;
    top: 112px;
    text-align: center;
  }
  .card-back .brand-name { color: var(--paper); font-size: 28px; }
  .card-back .brand-dot { background: var(--paper); width: 18px; height: 18px; }
  .card-back .brand-url { color: var(--paper); font-size: 13px; margin-top: 4px; }

  .card-front .card-logo {
    position: absolute;
    left: 0;
    right: 0;
    top: 44px;
    text-align: center;
  }
  .card-front .brand-name { font-size: 28px; }
  .card-front .brand-dot { width: 18px; height: 18px; }
  .card-front .brand-url { font-size: 13px; margin-top: 4px; }

  .holder {
    position: absolute;
    top: 148px;
    left: 0;
    right: 0;
    text-align: center;
  }
  .holder-name {
    font-size: 16px;
    font-weight: 400;
    letter-spacing: 1px;
    color: var(--brand-blue);
    text-transform: uppercase;
  }
  .holder-role {
    font-size: 12px;
    color: var(--ink-grey);
    margin-top: 2px;
  }
  .contact {
    position: absolute;
    left: 0;
    right: 0;
    bottom: 30px;
    text-align: center;
    font-size: 11.5px;
    line-height: 1.6;
    color: var(--ink-grey);
  }
  .contact-label { color: var(--brand-blue); }
</style>
</head>
<body>

  <div class="brand-lockup">
    <div class="brand-mark">
      <span class="brand-dot"></span>
      <span class="brand-name">ZOL QUENDARO</span>
    </div>
    <div class="brand-url">www.zolquendaro.com.sg</div>
  </div>

  <section class="card card-back" aria-label="Name card, reverse side">
    <svg class="card-decor" viewBox="0 0 500 290" aria-hidden="true">
      <circle cx="150" cy="250" r="120" fill="var(--card-blue-soft)"/>
      <circle cx="420" cy="150" r="150" fill="var(--card-blue-soft)"/>
    </svg>
    <div class="card-logo">
      <div class="brand-mark">
        <span class="brand-dot"></span>
        <span class="brand-name">ZOL QUENDARO</span>
      </div>
      <div class="brand-url">www.zolquendaro.com.sg</div>
    </div>
  </section>

  <section class="card card-front" aria-label="Name card, front side">
    <svg class="card-decor" viewBox="0 0 500 290" aria-hidden="true">
      <circle cx="20" cy="290" r="95" fill="var(--cloud-grey)"/>
      <circle cx="500" cy="40" r="90" fill="var(--cloud-grey)"/>
    </svg>
    <div class="card-logo">
      <div class="brand-mark">
        <span class="brand-dot"></span>
        <span class="brand-name">ZOL QUENDARO</span>
      </div>
      <div class="brand-url">www.zolquendaro.com.sg</div>
    </div>
    <div class="holder">
      <div class="holder-name">Maren Holloway</div>
      <div class="holder-role">Managing Director</div>
    </div>
    <div class="contact">
      <div>48 Telford Row, Harbour Court, Singapore 058112</div>
      <div>
        <span class="contact-label">T:</span> +65 600 18735 ·
        <span class="contact-label">M:</span> +971 555 218 907 ·
        <span class="contact-label">E:</span> info@zolquendaro.com.sg
      </div>
    </div>
  </section>

</body>
</html>
```